eBook Cover_H. Brückner-Lohm
Schnell und zuverlässoig,Änderungswünsche wurden umgehend ausgeführt. Vielen Dank für das tolle Cover zu meinem ersten Buch!
Zielgruppe
freie Roman-Autorin (Erstlingswerk)
Zielgruppe: Lesende (Erwachsene), Frauen
Charakterisierung: magisch-realistischer Familienroman, spielt im Europa der Jetzt-Zeit
Aufgabenstellung
Im ersten Schritt geht es um ein Cover für ein eBook, das aber bei Bedarf als Book on Demand gedruckt werden soll. Es wird daher später Anforderung bzgl. Dicke / Umfang des gedruckten Buches und einer Rückseite geben. Das gewählte Design soll dann dahingehend überarbeitet und finale Druckdaten zur Verfügung gestellt werden. Dies soll von vornherein berücksichtigt werden und im Preis enthalten sein.
Titel: Moos auf Moos, Wellen aus Glas
Autorinnenname: Hanna Brückner-Lohm
des weiteren auf dem Cover: Roman

```html
<!DOCTYPE html>
<html lang="de">
<head>
<meta charset="utf-8">
<title>Moos auf Moos, Wellen aus Glas – Hanna Brückner-Lohm</title>
<link rel="stylesheet" href="https://fonts.googleapis.com/css2?family=Open+Sans:wght@400&family=Rubik+Distressed&display=swap">
<style>
  :root {
    --bg-deep: #0b0b0b;
    --bg-soft: #1b1b1b;
    --ink-light: #f2f2f2;
    --ink-muted: #d9d9d9;
    --title-orange: #eda322;
    --powder-core: #f4f4f4;
    --powder-mid: #a0a0a0;
  }
  * { margin: 0; padding: 0; box-sizing: border-box; }
  html, body {
    width: 800px;
    height: 1200px;
    overflow: hidden;
    background: var(--bg-deep);
  }
  .cover {
    position: relative;
    width: 800px;
    height: 1200px;
    overflow: hidden;
    background:
      radial-gradient(ellipse 70% 50% at 60% 40%, var(--bg-soft) 0%, var(--bg-deep) 70%),
      var(--bg-deep);
  }
  .author {
    position: absolute;
    top: 112px;
    left: 0;
    width: 100%;
    text-align: center;
    font-family: "Open Sans", Arial, sans-serif;
    font-weight: 400;
    font-size: 33px;
    letter-spacing: 0.3px;
    color: var(--ink-light);
  }
  .title {
    position: absolute;
    top: 292px;
    left: 170px;
    width: 610px;
    text-align: center;
    font-family: "Rubik Distressed", "Arial Rounded MT Bold", sans-serif;
    font-weight: 400;
    font-size: 58px;
    line-height: 78px;
    letter-spacing: 1px;
    white-space: nowrap;
    color: var(--title-orange);
  }
  .title span { display: block; }
  .powder-burst {
    position: absolute;
    left: 0;
    top: 530px;
    width: 780px;
    height: 650px;
  }
  .genre {
    position: absolute;
    right: 58px;
    bottom: 46px;
    font-family: "Open Sans", Arial, sans-serif;
    font-size: 20px;
    color: var(--ink-muted);
  }
</style>
</head>
<body>
  <main class="cover">
    <p class="author">Hanna Brückner-Lohm</p>
    <h1 class="title"><span>Moos auf Moos,</span><span>Wellen aus Glas</span></h1>
    <svg class="powder-burst" viewBox="0 0 780 650" role="img" aria-label="Explodierende weiße Pulverwolke auf schwarzem Grund">
      <defs>
        <radialGradient id="burst-glow" cx="50%" cy="50%" r="50%">
          <stop offset="0%" stop-color="var(--powder-core)" stop-opacity="0.95"/>
          <stop offset="40%" stop-color="var(--powder-core)" stop-opacity="0.7"/>
          <stop offset="70%" stop-color="var(--powder-mid)" stop-opacity="0.3"/>
          <stop offset="100%" stop-color="var(--powder-mid)" stop-opacity="0"/>
        </radialGradient>
      </defs>
      <ellipse cx="380" cy="320" rx="380" ry="300" fill="url(#burst-glow)"/>
    </svg>
    <p class="genre">Roman</p>
  </main>
</body>
</html>
```